Dietetic office: Bright Plate

I want to give my business card a modern and warm look (which attracts the eye and has a reassuring side), which links dietetics to a moment of well-being. The front and back sides must be used (not just to put the logo on the front side)

The map should be eye-catching and easy to read. I don't necessarily want to have a plain background, which I find visually weighs down the maps.
I really like the square format of a business card with rounded edges which is different from what we are used to finding (and why not take this square diagonally?), however I am not closed to another format as long as I like the style.

Who am I? Mireille, 32 years old, Dietician and passionate about food since always. I am specialized in slimming and an expert in micro nutrition, which means that I take into account not only the nutritional balance while maintaining pleasure (if foods are present in the business card, I do not want some cliché things where there would just be fruits and vegetables, but really something more global), but also the psycho-emotional dimension that I will treat with food supplements based on plants, fruits or vegetables.

-----------------------------------------------------------------------------------

 Mention to appear on the card IN FRENCH (please be careful in case of translation that the use of words is correct):

Mireille DORAN
Dietician Nutritionist
Expert in Slimming and Micro-Nutrition

Slogan: I help you lose weight sustainably with pleasure and by reconciling your events

Catchphrases: Want to lose weight? Do you like going out? Do you have a lot of events? And is pleasure on your plate important to you?

Make an appointment on Rendiplan or on 06 41 58 30 92
mireille.brightplate@exemplo-mail.fr
Address: Health Center, Rue des Glycines, 13480 Calvelle
www.brightplate-exemple.fr
Friendwall + Picturo Logo

- The company logo has been uploaded for your viewing. Other file formats can be made available if required.
- I would like a place for a photo of me to be possible.

Good morning,
I want to have a business card that is both lively and warm. Which will easily catch the eye while being easy to read and make people understand that I am in the field of well-being.
I like the square side in business cards (and why not use them diagonally?), or a more classic but original one.
Both the front and back sides must be used (I don't want to have the logo on just one side)
I don't want to have a plain background, but rather something more muted (I really like the suggestion from "Reed Cloud Graphic Designer" for this)
the use of logo for telephone, mail, address, rendiplan, friendwall, pictu etc is possible in order to facilitate reading

Please follow the various elements of the brief regarding the text and use the French text as it is.

I like business cards preferably square (with the possibility of using them diagonally).
The map should be eye-catching and easy to read.
It must bring pep while having softness which brings back to the well-being side
The card must be used on the front and back for the different elements (I do not want to have only the logo on the front side)
The text must correspond to the brief (be careful with the translation which can sometimes be bad)
I don't want to have a plain blue or orange background. I really like the idea of the background from "Reed Cloud Graphic Designer"

You can if you wish use symbols for contacts, telephone, rendiplan, address, fw, pictu....

Target Market(s)

mainly women between 25 and 65 years old + men around 40 years old

Contact Information for Business Card

Font styles to use
Sans Serif
Script

Colors
0054AA
0677BA
7BADD7
CADEEF
E8F1F8
0094D4
00A9DD
6FCCEA
C7EBF8
E9F6FB
00AB8E
00BBA5
67D7C9
C6EFE9
E9F9F6
FFC000
F8CF3A
FAE287
FDF2CF
FEFAEE
F0912C
F2A743
F7CA91
FBE8D2
FDF5EE

Requirements
Must have
• some pep! while being refined
Nice to have
• I really like the square format of a business card with rounded edges which is different from what we are used to finding, however I am not closed to another format as long as I like the style.
Should not have
• if foods are represented, only show fruits and vegetables (too cliché)

```html
<!DOCTYPE html>
<html lang="en">
<head>
<meta charset="utf-8">
<title>Bright Plate – Business Card</title>
<link href="https://fonts.googleapis.com/css2?family=Source+Sans+3:wght@400;600;700;800&family=Kalam:wght@700&display=swap" rel="stylesheet">
<style>
  :root {
    --stage: #0e4266;
    --frame-light: #14cfe0;
    --frame-deep: #0a80d8;
    --orange: #ff8c00;
    --blue-text: #0a78cc;
    --navy-text: #0054aa;
    --white: #ffffff;
  }
  * { box-sizing: border-box; margin: 0; padding: 0; }
  html, body { width: 1200px; height: 1200px; overflow: hidden; }
  body {
    background: var(--stage);
    font-family: "Source Sans 3", sans-serif;
    position: relative;
  }
  .card {
    position: absolute;
    top: 353px;
    width: 496px;
    height: 496px;
    border-radius: 70px;
    background: linear-gradient(135deg, var(--frame-light) 0%, var(--frame-deep) 55%, var(--frame-light) 100%);
  }
  .card--front { left: 82px; }
  .card--back { left: 620px; }
  .card__face {
    position: absolute;
    inset: 25px;
    background: var(--white);
    border-radius: 46px;
  }

  /* front */
  .social {
    position: absolute;
    top: 40px;
    right: 24px;
    display: flex;
    gap: 16px;
    color: var(--orange);
    font-weight: 700;
    font-size: 16px;
  }
  .social__item { display: flex; align-items: center; gap: 5px; }
  .social__dot { width: 10px; height: 10px; border-radius: 50%; background: var(--orange); }
  .brand {
    position: absolute;
    top: 186px;
    left: 0; right: 0;
    text-align: center;
    color: var(--blue-text);
    font-weight: 600;
    font-size: 58px;
    line-height: 1;
  }
  .site {
    position: absolute;
    top: 354px;
    left: 0; right: 0;
    text-align: center;
    color: var(--orange);
    font-weight: 800;
    font-size: 21px;
    letter-spacing: 0.5px;
  }

  /* back */
  .identity {
    position: absolute;
    top: 52px;
    left: 37px;
    display: flex;
    align-items: center;
  }
  .identity__name {
    color: var(--orange);
    font-weight: 600;
    font-size: 31px;
    line-height: 1;
  }
  .identity__role {
    color: var(--navy-text);
    font-weight: 700;
    font-size: 14px;
    letter-spacing: 2px;
    margin-top: 5px;
  }
  .identity__rule {
    width: 2px;
    height: 50px;
    background: var(--orange);
    margin: 0 12px 0 14px;
  }
  .identity__expertise {
    color: var(--blue-text);
    font-size: 17px;
    line-height: 1.2;
  }
  .slogan {
    position: absolute;
    top: 120px;
    left: 20px;
    width: 414px;
    height: 54px;
    background: var(--orange);
    border-radius: 10px;
    text-align: center;
    color: var(--white);
    font-family: "Kalam", cursive;
    font-weight: 700;
    font-size: 17px;
    line-height: 21px;
    padding-top: 6px;
  }
  .questions {
    position: absolute;
    top: 186px;
    left: 37px;
    list-style: none;
    color: var(--blue-text);
    font-weight: 600;
    font-size: 17px;
    line-height: 21px;
  }
  .booking-lead {
    position: absolute;
    top: 274px;
    left: 37px;
    color: var(--orange);
    font-weight: 600;
    font-size: 17px;
  }
  .booking {
    position: absolute;
    top: 306px;
    left: 29px;
    display: flex;
    align-items: center;
    gap: 7px;
  }
  .pill {
    background: var(--orange);
    color: var(--white);
    font-weight: 600;
    font-size: 27px;
    line-height: 30px;
    padding: 0 9px;
    border-radius: 16px;
  }
  .booking__or { color: var(--blue-text); font-weight: 600; font-size: 21px; }
  .email {
    position: absolute;
    top: 349px;
    left: 66px;
    width: 320px;
    height: 30px;
    border-radius: 15px;
    background: var(--frame-deep);
    color: var(--white);
    font-weight: 600;
    font-size: 16px;
    line-height: 30px;
    text-align: center;
  }
  .address {
    position: absolute;
    top: 396px;
    left: 0; right: 0;
    text-align: center;
    color: var(--orange);
    font-weight: 700;
    font-size: 16px;
  }
</style>
</head>
<body>

<section class="card card--front">
  <div class="card__face">
    <div class="social">
      <span class="social__item"><span class="social__dot"></span>Picturo</span>
      <span class="social__item"><span class="social__dot"></span>Friendwall</span>
    </div>
    <div class="brand">Bright Plate</div>
    <div class="site">WWW.BRIGHTPLATE-EXEMPLE.FR</div>
  </div>
</section>

<section class="card card--back">
  <div class="card__face">
    <div class="identity">
      <div>
        <div class="identity__name">Mireille DORAN</div>
        <div class="identity__role">DIETICIAN NUTRITIONIST</div>
      </div>
      <div class="identity__rule"></div>
      <div class="identity__expertise">Expert in Slimming<br>and Micro-Nutrition</div>
    </div>

    <p class="slogan">I help you lose weight sustainably with pleasure<br>and by reconciling your events</p>

    <ul class="questions">
      <li>Want to lose weight?</li>
      <li>Do you like going out?</li>
      <li>Do you have a lot of events?</li>
      <li>And pleasure on your plate is important for you ?</li>
    </ul>

    <div class="booking-lead">Make an appointment on</div>
    <div class="booking">
      <span class="pill">RENDIPLAN</span>
      <span class="booking__or">or on</span>
      <span class="pill">06 41 58 30 92</span>
    </div>

    <div class="email">mireille.brightplate@exemplo-mail.fr</div>
    <div class="address">Health Center, Rue des Glycines, 13480 Calvelle</div>
  </div>
</section>

</body>
</html>
```